Organic Herbs & Spices container

Greek startup company, which cultivate and trade spices and herbs (such as oregano, mint, thyme, sage etc.)

At present we are interested in only the type and shape of packaging which should be made by materials such as paper, cardboard, laminated paper and others based on paper or plastic.

Package size vary from 80g (2.82oz) - 300g (10.58oz). We are going to use the same packing for a variety of products with different information

* Please find attached our logo which should be included in the design.
* There is no company name available at the moment, however a name placeholder should be included.
* include a placeholder for the type of product (sage, oregano, mint, tea etc...).
* Each package should have a place in order to include product details and nutrition facts.

e.g.
xxxx (company name placeholder)
Sage (product type)
product details and nutrition facts.
Updates

Dear designers,first of all, thank you for your proposals. Please find bellow some updates for the project.- It is mandatory to include the logo into the design - Each package should be able to stored vertically - We are looking for one specific package design, please do not submit many variations of a certain package neither colour differentiations Thanks and good luck Added Wednesday, September 28, 2016

Please avoid the use of images. The same package will be used for all the kinds of products (only name and maybe colour will be different among different products. A transparent frame that will show the contents could be used too) Added Wednesday, September 28, 2016

Please find attached logo in EPS format

Our logo is the baseline, any concepts should be based on it. Try to avoid just adding the logo as a small sticker somewhere on the design. Please try to create around it at any way toy like. This could be, to visualize it as a 3D shape or object which can be used as the container of the products.

Reason: We would like to extend the time of the project. We believe that most of the submitted designs do not comply with our requirements.

Reason: We would like to see a bigger variety of ideas

Target Market(s)

Pretty much to anyone over 20 years old worldwide.

Industry/Entity Type

Nutrition

Requirements
Must have
• It should be attractive, easily recognized, simple yet innovative, durable, functional (easy to use) and easy to store.
Should not have
• Project must not include complex or obnoxious shapes and colours.

```html
<!DOCTYPE html>
<html lang="en">
<head>
<meta charset="utf-8">
<title>Herb &amp; Spice Tube Range</title>
<link href="https://fonts.googleapis.com/css2?family=Open+Sans:wght@700&family=Yellowtail&display=swap" rel="stylesheet">
<style>
  :root{
    --page:#ffffff;
    --cork:#b98d5e;
    --cork-dark:#9c7448;
    --brand-green:#1d7a2f;
    --label-white:#ffffff;
    --glass-edge:#e3e6e6;

    --salt-base:#bfe6ea;
    --salt-band:#74cfd6;
    --salt-panel:#4fa8aa;
    --salt-fill:#eef1f1;

    --oregano-base:#12301a;
    --oregano-band:#3d7a50;
    --oregano-panel:#06200b;
    --oregano-fill:#7d8a4c;

    --mint-base:#8dd08d;
    --mint-band:#3a9a48;
    --mint-panel:#2e8f3e;
    --mint-fill:#3f6a36;

    --chamomile-base:#a4c86e;
    --chamomile-band:#3f8a4a;
    --chamomile-panel:#3f804e;
    --chamomile-fill:#b9c18e;
  }
  *{margin:0;padding:0;box-sizing:border-box}
  html,body{width:1200px;height:781px;overflow:hidden;background:var(--page)}
  .range{position:relative;width:1200px;height:781px}

  .tube{position:absolute;top:118px;width:143px;height:542px}
  .tube--salt{left:165px}
  .tube--oregano{left:410px}
  .tube--mint{left:652px}
  .tube--chamomile{left:893px}

  .tube__cork{position:absolute;left:0;top:0;width:143px;height:34px;
    background:linear-gradient(var(--cork),var(--cork-dark));border-radius:6px 6px 0 0}

  .tube__label{position:absolute;left:0;top:32px;width:143px;height:312px;overflow:hidden}
  .tube__label-ground{position:absolute;inset:0}

  .brand-tag{position:absolute;left:31px;top:5px;width:80px;height:62px;background:var(--label-white);
    display:flex;flex-direction:column;align-items:center;justify-content:center;gap:6px}
  .brand-tag__dot{width:18px;height:18px;border-radius:50%;background:var(--brand-green)}
  .brand-tag__name{font-family:'Open Sans',sans-serif;font-weight:700;font-size:9.5px;color:var(--brand-green);letter-spacing:.2px}

  .product-panel{position:absolute;left:32px;top:102px;width:79px;height:210px;
    display:flex;align-items:center;justify-content:center}
  .product-panel__name{font-family:'Yellowtail',cursive;color:#fff;font-size:50px;line-height:1;
    writing-mode:vertical-rl;transform:rotate(180deg);white-space:nowrap}
  .product-panel__name--long{font-size:38px}

  .tube__window{position:absolute;left:0;top:344px;width:143px;height:198px;
    border-radius:0 0 10px 10px;border:1px solid var(--glass-edge);border-top:none}

  .tube--salt .tube__label-ground{background:linear-gradient(135deg,var(--salt-base),var(--salt-band) 50%,var(--salt-base))}
  .tube--salt .product-panel{background:var(--salt-panel)}
  .tube--salt .tube__window{background:var(--salt-fill)}

  .tube--oregano .tube__label-ground{background:linear-gradient(135deg,var(--oregano-base),var(--oregano-band) 50%,var(--oregano-base))}
  .tube--oregano .product-panel{background:var(--oregano-panel)}
  .tube--oregano .tube__window{background:var(--oregano-fill)}

  .tube--mint .tube__label-ground{background:linear-gradient(135deg,var(--mint-base),var(--mint-band) 50%,var(--mint-base))}
  .tube--mint .product-panel{background:var(--mint-panel)}
  .tube--mint .tube__window{background:var(--mint-fill)}

  .tube--chamomile .tube__label-ground{background:linear-gradient(135deg,var(--chamomile-base),var(--chamomile-band) 50%,var(--chamomile-base))}
  .tube--chamomile .product-panel{background:var(--chamomile-panel)}
  .tube--chamomile .tube__window{background:var(--chamomile-fill)}
</style>
</head>
<body>
<main class="range">

  <section class="tube tube--salt">
    <div class="tube__cork"></div>
    <div class="tube__label">
      <div class="tube__label-ground" role="img" aria-label="Diagonal aqua stripe pattern on the label"></div>
      <div class="brand-tag"><span class="brand-tag__dot"></span><span class="brand-tag__name">BRAND NAME</span></div>
      <div class="product-panel"><span class="product-panel__name">Salt</span></div>
    </div>
    <div class="tube__window" role="img" aria-label="Fine white salt visible through the clear tube"></div>
  </section>

  <section class="tube tube--oregano">
    <div class="tube__cork"></div>
    <div class="tube__label">
      <div class="tube__label-ground" role="img" aria-label="Diagonal dark green stripe pattern on the label"></div>
      <div class="brand-tag"><span class="brand-tag__dot"></span><span class="brand-tag__name">BRAND NAME</span></div>
      <div class="product-panel"><span class="product-panel__name">Oregano</span></div>
    </div>
    <div class="tube__window" role="img" aria-label="Dried oregano flakes visible through the clear tube"></div>
  </section>

  <section class="tube tube--mint">
    <div class="tube__cork"></div>
    <div class="tube__label">
      <div class="tube__label-ground" role="img" aria-label="Diagonal mint green stripe pattern on the label"></div>
      <div class="brand-tag"><span class="brand-tag__dot"></span><span class="brand-tag__name">BRAND NAME</span></div>
      <div class="product-panel"><span class="product-panel__name">Mint</span></div>
    </div>
    <div class="tube__window" role="img" aria-label="Dried mint leaves visible through the clear tube"></div>
  </section>

  <section class="tube tube--chamomile">
    <div class="tube__cork"></div>
    <div class="tube__label">
      <div class="tube__label-ground" role="img" aria-label="Diagonal olive and yellow stripe pattern on the label"></div>
      <div class="brand-tag"><span class="brand-tag__dot"></span><span class="brand-tag__name">BRAND NAME</span></div>
      <div class="product-panel"><span class="product-panel__name product-panel__name--long">Chamomile</span></div>
    </div>
    <div class="tube__window" role="img" aria-label="Dried chamomile buds visible through the clear tube"></div>
  </section>

</main>
</body>
</html>
```